Business Card Design

Need a new business card to represent our legal vertical focus. attached is an example of our old business card and newest logo. we would like the card to also identify "Legal Tech" as a tag line of business.

Our new address is
7381 Harrowgate Linden Rd.
Suite 418
Cincinnati, OH 45917

we no longer have a fax number.

Target Market(s)

Tech Consulting for Law Firms

Industry/Entity Type

Legal

Contact Information for Business Card

should use logo and colors. we are a b2b company

Other font styles liked:
• tahoma

Requirements
Must have
• all print should be in lower case just as shown in photos. tag line should not
Should not have
• pinstripes or drop shadows

```html
<!DOCTYPE html>
<html lang="en">
<head>
<meta charset="utf-8">
<title>BraidLink Legal Tech – Business Card</title>
<link href="https://fonts.googleapis.com/css2?family=Open+Sans:wght@400;600;700&display=swap" rel="stylesheet">
<style>
  :root {
    --backdrop: #8c8c8c;
    --navy: #233a83;
    --orange: #e84c22;
    --white: #ffffff;
    --grey-text: #6d6d6d;
    --card-w: 600px;
    --card-h: 343px;
  }
  * { box-sizing: border-box; margin: 0; padding: 0; }
  html, body {
    width: 1200px; height: 900px; overflow: hidden;
    background: var(--backdrop);
    font-family: "Open Sans", Tahoma, sans-serif;
  }
  .stage {
    width: 1200px; height: 900px;
    display: flex; flex-direction: column; align-items: center; justify-content: center;
    gap: 50px;
  }
  .card {
    position: relative;
    width: var(--card-w); height: var(--card-h);
    overflow: hidden;
  }

  /* Back side */
  .card--back { background: var(--orange); }
  .card--back .band-navy {
    position: absolute; left: 0; right: 0; top: 42px; height: 238px;
    background: var(--navy);
  }
  .brand {
    position: absolute; display: flex; align-items: center; gap: 12px;
  }
  .brand__dot { width: 22px; height: 22px; border-radius: 50%; }
  .brand__name { font-weight: 700; font-size: 50px; line-height: 1; letter-spacing: -0.5px; }
  .tagline {
    position: absolute; font-size: 19px; letter-spacing: 1.5px;
  }
  .card--back .brand { left: 150px; top: 110px; }
  .card--back .brand__dot { background: var(--white); }
  .card--back .brand__name { color: var(--white); }
  .card--back .tagline { right: 120px; top: 176px; color: var(--white); }

  /* Front side */
  .card--front { background: var(--white); }
  .card--front .band-orange {
    position: absolute; left: 0; right: 0; top: 150px; height: 167px;
    background: var(--orange);
  }
  .card--front .band-navy {
    position: absolute; left: 0; right: 0; bottom: 0; height: 26px;
    background: var(--navy);
  }
  .card--front .brand { left: 180px; top: 48px; }
  .card--front .brand__dot { background: var(--orange); }
  .card--front .brand__name { color: var(--navy); }
  .card--front .tagline { right: 70px; top: 113px; color: var(--grey-text); }

  .person { position: absolute; left: 34px; top: 164px; color: var(--white); }
  .person__name { font-weight: 700; font-size: 22px; line-height: 1.1; }
  .person__title { font-size: 15px; }

  .contacts {
    position: absolute; right: 28px; top: 196px;
    list-style: none; color: var(--white); font-size: 15.5px; line-height: 22px;
  }
  .contacts li { display: flex; justify-content: flex-end; align-items: center; gap: 10px; }
  .contacts svg { width: 13px; height: 13px; fill: var(--white); flex: none; }
</style>
</head>
<body>
<main class="stage">
  <section class="card card--back" aria-label="Card back">
    <div class="band-navy"></div>
    <div class="brand"><span class="brand__dot"></span><span class="brand__name">BraidLink</span></div>
    <div class="tagline">Legal Tech</div>
  </section>

  <section class="card card--front" aria-label="Card front">
    <div class="band-orange"></div>
    <div class="band-navy"></div>
    <div class="brand"><span class="brand__dot"></span><span class="brand__name">BraidLink</span></div>
    <div class="tagline">Legal Tech</div>

    <div class="person">
      <div class="person__name">marcus hale</div>
      <div class="person__title">managing director</div>
    </div>

    <ul class="contacts">
      <li>123.456.7890
        <svg viewBox="0 0 16 16"><path d="M3 1h3l1.5 4-2 1.2a9 9 0 0 0 4.3 4.3L11 8.5l4 1.5v3c0 1-1 2-2 2A13 13 0 0 1 1 3c0-1 1-2 2-2z"/></svg></li>
      <li>123.456.7890
        <svg viewBox="0 0 16 16"><path d="M4 0h8a1 1 0 0 1 1 1v14a1 1 0 0 1-1 1H4a1 1 0 0 1-1-1V1a1 1 0 0 1 1-1zm1 2v10h6V2zm3 11a1 1 0 1 0 0 2 1 1 0 0 0 0-2z"/></svg></li>
      <li>info@youremail.com
        <svg viewBox="0 0 16 16"><path d="M0 3h16v10H0zm1.5 1.5v.4L8 9l6.5-4.1v-.4z"/></svg></li>
      <li>www.website.com
        <svg viewBox="0 0 16 16"><path d="M6.5 9.5l3-3 1 1-3 3zM4 7l2-2 1.2 1.2-2 2a1.4 1.4 0 0 0 2 2l2-2L10.4 9.4l-2 2a3.1 3.1 0 0 1-4.4-4.4zm8 2l-2 2-1.2-1.2 2-2a1.4 1.4 0 0 0-2-2l-2 2L5.6 6.6l2-2A3.1 3.1 0 0 1 12 9z"/></svg></li>
      <li>7381 harrowgate linden rd., suite 418, cincinnati, oh 45917
        <svg viewBox="0 0 16 16"><path d="M8 0a5.5 5.5 0 0 1 5.5 5.5C13.5 10 8 16 8 16S2.5 10 2.5 5.5A5.5 5.5 0 0 1 8 0zm0 3.3a2.2 2.2 0 1 0 0 4.4 2.2 2.2 0 0 0 0-4.4z"/></svg></li>
    </ul>
  </section>
</main>
</body>
</html>
```